Bramblegate Card Company Business Cards

We are a trading card store with Zorvanix, sports and other TCG cards, we need a business card design that encompasses a clean cut, modern style with a retro flare. website is bramblegatecardco.example for reference. Can utilize a comic book era feel or a more modern outdoor feel to utilize the "Pacific Northwest" elements of tress, mountains, etc.

Industry/Entity Type

Trading cards and collectibles

Contact Information for Business Card

business name, email address, phone number, name, owner job title

Font styles to use
Sans Serif

```html
<!DOCTYPE html>
<html lang="en">
<head>
<meta charset="utf-8">
<title>Bramblegate Card Company – Business Cards</title>
<link href="https://fonts.googleapis.com/css2?family=Nunito+Sans:wght@400;800;900&display=swap" rel="stylesheet">
<style>
  :root {
    --backdrop: #d1d2d4;
    --card: #ffffff;
    --slate: #707071;
    --cyan: #12bce0;
    --ink: #2b2b2b;
    --rule: #6f6f70;
  }
  * { box-sizing: border-box; margin: 0; padding: 0; }
  html, body {
    width: 900px; height: 1200px; overflow: hidden;
    background: var(--backdrop);
    font-family: "Nunito Sans", Arial, sans-serif;
  }
  .canvas { position: relative; width: 900px; height: 1200px; }
  .card {
    position: absolute; left: 135px; width: 630px; height: 357px;
    background: var(--card); border-radius: 14px;
    box-shadow: 4px 6px 8px rgba(0,0,0,0.18);
  }
  .card--front { top: 215px; }
  .card--back { top: 628px; }

  .brand {
    position: absolute; display: flex; flex-direction: column;
    align-items: center; justify-content: center; text-align: center;
  }
  .brand__dot { border-radius: 50%; background: var(--cyan); flex: none; }
  .brand__name {
    color: var(--slate); font-weight: 900; text-transform: uppercase;
    line-height: 1.05; letter-spacing: 1.5px; white-space: nowrap;
  }

  .card--front .brand { left: 0; right: 0; top: 0; bottom: 0; gap: 18px; }
  .card--front .brand__dot { width: 64px; height: 64px; }
  .card--front .brand__name { font-size: 38px; }

  .card--back .brand { left: 68px; width: 250px; top: 0; bottom: 0; gap: 12px; }
  .card--back .brand__dot { width: 40px; height: 40px; }
  .card--back .brand__name { font-size: 23px; }

  .divider {
    position: absolute; left: 315px; top: 112px;
    width: 2px; height: 134px; background: var(--rule);
  }
  .contact { position: absolute; left: 340px; top: 112px; }
  .contact__name {
    color: var(--cyan); font-weight: 800; font-size: 25px;
    text-transform: uppercase; line-height: 1.1; letter-spacing: 0.3px;
  }
  .contact__title { color: var(--ink); font-size: 14.5px; margin-top: 4px; }
  .contact__accent { width: 44px; height: 2px; background: var(--cyan); margin: 5px 0 9px; }
  .contact__list { list-style: none; }
  .contact__item {
    display: flex; align-items: center; gap: 6px;
    color: var(--ink); font-size: 14.5px; height: 25px; white-space: nowrap;
  }
  .contact__item--phone { letter-spacing: 2px; }
  .icon { width: 15px; height: 15px; flex: none; fill: var(--cyan); }
</style>
</head>
<body>
<main class="canvas">
  <section class="card card--front" aria-label="Card front">
    <div class="brand">
      <span class="brand__dot" aria-hidden="true"></span>
      <h1 class="brand__name">Bramblegate<br>Card Company</h1>
    </div>
  </section>

  <section class="card card--back" aria-label="Card back">
    <div class="brand">
      <span class="brand__dot" aria-hidden="true"></span>
      <p class="brand__name">Bramblegate<br>Card Company</p>
    </div>
    <div class="divider"></div>
    <div class="contact">
      <h2 class="contact__name">Delmar Quist</h2>
      <p class="contact__title">Owner</p>
      <div class="contact__accent"></div>
      <ul class="contact__list">
        <li class="contact__item contact__item--phone">
          <svg class="icon" viewBox="0 0 24 24" aria-hidden="true"><path d="M6.6 10.8a15.1 15.1 0 0 0 6.6 6.6l2.2-2.2c.3-.3.7-.4 1-.2 1.1.4 2.3.6 3.6.6.6 0 1 .4 1 1V20c0 .6-.4 1-1 1A17 17 0 0 1 3 4c0-.6.4-1 1-1h3.5c.6 0 1 .4 1 1 0 1.3.2 2.5.6 3.6.1.3 0 .7-.2 1z"/></svg>
          1 (555) 014-2270
        </li>
        <li class="contact__item">
          <svg class="icon" viewBox="0 0 24 24" aria-hidden="true"><path d="M2 5h20v14H2z"/><path d="M2 6l10 8 10-8" fill="none" stroke="#fff" stroke-width="1.6"/></svg>
          info@bramblegatecardco.example
        </li>
        <li class="contact__item">
          <svg class="icon" viewBox="0 0 24 24" aria-hidden="true"><g fill="none" stroke="var(--cyan)" stroke-width="1.8"><circle cx="12" cy="12" r="9.5"/><ellipse cx="12" cy="12" rx="4" ry="9.5"/><path d="M2.5 12h19M4 7h16M4 17h16"/></g></svg>
          bramblegatecardco.example
        </li>
      </ul>
    </div>
  </section>
</main>
</body>
</html>
```